Law Office Business Card

We need a business card design to include the following information:
Name of Firm: Brennick Law Group, P.A.
Address: 4627 Sandlot Ave, Ste 208, Coral Mesa, FL 33999
Phone: 561-555-0148
Fax: 561-555-0193
Website: http://www.tbrennicklaw.example

We Need a place for the Person's name and email address. Please start with the following:
Lorna K. Dwyer, Esq.
lorna@tbrennicklaw.example

```html
<!DOCTYPE html>
<html lang="en">
<head>
<meta charset="utf-8">
<title>Brennick Law Group – Business Card</title>
<link href="https://fonts.googleapis.com/css2?family=Arimo:wght@400;700&display=swap" rel="stylesheet">
<style>
  :root {
    --backdrop: #e8e4de;
    --card-white: #ffffff;
    --taupe-dark: #857a6f;
    --taupe-khaki: #b3aa94;
    --ink-dark: #3f3a35;
    --ink-soft: #8d847a;
    --ink-light: #f6f3ee;
  }
  * { margin: 0; padding: 0; box-sizing: border-box; }
  html, body {
    width: 1200px;
    height: 1021px;
    overflow: hidden;
    background: var(--backdrop);
    font-family: "Arimo", Arial, sans-serif;
  }
  .canvas {
    position: relative;
    width: 1200px;
    height: 1021px;
  }
  .business-card {
    position: absolute;
    left: 100px;
    top: 224px;
    width: 1000px;
    height: 572px;
    background: var(--card-white);
    overflow: hidden;
    box-shadow: 0 18px 40px rgba(60, 50, 40, 0.25);
  }
  .card-bands {
    position: absolute;
    inset: 0;
    width: 1000px;
    height: 572px;
  }
  .band-dark { fill: var(--taupe-dark); }
  .band-khaki { fill: var(--taupe-khaki); }
  .band-rule { fill: none; stroke: var(--card-white); stroke-width: 4; }

  .attorney {
    position: absolute;
    right: 70px;
    top: 96px;
    text-align: right;
    color: var(--ink-dark);
  }
  .attorney-name {
    font-size: 32px;
    font-weight: 700;
    letter-spacing: 0.3px;
  }
  .attorney-title {
    font-size: 20px;
    color: var(--ink-soft);
    margin-top: 2px;
  }

  .firm-mark {
    position: absolute;
    left: 100px;
    top: 200px;
    display: flex;
    align-items: center;
    gap: 22px;
  }
  .firm-square {
    flex: none;
    width: 74px;
    height: 74px;
    border: 3px solid var(--taupe-khaki);
  }
  .firm-name {
    font-size: 38px;
    font-weight: 400;
    letter-spacing: 4px;
    text-transform: uppercase;
    color: var(--taupe-dark);
    line-height: 1.15;
    white-space: nowrap;
  }

  .office-address {
    position: absolute;
    left: 70px;
    top: 426px;
    color: var(--ink-light);
    font-size: 26px;
    font-style: normal;
    line-height: 1.3;
  }

  .contact-list {
    position: absolute;
    right: 34px;
    top: 386px;
    list-style: none;
    color: var(--ink-light);
    font-size: 20px;
  }
  .contact-item {
    display: flex;
    align-items: center;
    justify-content: flex-end;
    gap: 14px;
    height: 36px;
  }
  .contact-icon {
    flex: none;
    width: 26px;
    height: 26px;
  }
  .icon-disc { fill: var(--ink-light); }
  .icon-glyph { fill: var(--taupe-dark); }
  .icon-line { fill: none; stroke: var(--taupe-dark); stroke-width: 1.5; }
  .icon-cut { fill: none; stroke: var(--ink-light); stroke-width: 1.5; }
</style>
</head>
<body>
<main class="canvas">
  <article class="business-card">
    <svg class="card-bands" viewBox="0 0 1000 572" aria-hidden="true">
      <!-- top band with inset rule -->
      <polygon class="band-dark" points="0,0 1000,0 1000,54 540,54 490,94 0,94"/>
      <polyline class="band-rule" points="34,78 482,78 532,38 1000,38"/>
      <!-- left edge -->
      <rect class="band-dark" x="0" y="0" width="34" height="572"/>
      <!-- address band with inset rule -->
      <polygon class="band-khaki" points="34,400 612,400 548,572 34,572"/>
      <polyline class="band-rule" points="34,414 592,414"/>
      <!-- bottom edge -->
      <rect class="band-dark" x="0" y="552" width="1000" height="20"/>
      <!-- contact panel -->
      <polygon class="band-dark" points="652,360 1000,360 1000,572 576,572"/>
    </svg>

    <header class="attorney">
      <h1 class="attorney-name">Lorna K. Dwyer,</h1>
      <p class="attorney-title">Esq.</p>
    </header>

    <div class="firm-mark">
      <span class="firm-square"></span>
      <p class="firm-name">Brennick Law Group, P.A.</p>
    </div>

    <address class="office-address">
      4627 Sandlot Ave,<br>
      Ste 208,<br>
      Coral Mesa, FL 33999
    </address>

    <ul class="contact-list">
      <li class="contact-item">
        <span>561-555-0148</span>
        <svg class="contact-icon" viewBox="0 0 26 26" aria-label="Phone">
          <circle class="icon-disc" cx="13" cy="13" r="13"/>
          <path class="icon-glyph" d="M9 7 l3 0 l1 4 l-2 1 q1.5 3 4 4 l1-2 l4 1 l0 3 q-8 1-11-11z"/>
        </svg>
      </li>
      <li class="contact-item">
        <span>561-555-0193</span>
        <svg class="contact-icon" viewBox="0 0 26 26" aria-label="Fax">
          <circle class="icon-disc" cx="13" cy="13" r="13"/>
          <rect class="icon-glyph" x="9" y="6" width="8" height="5"/>
          <rect class="icon-glyph" x="6" y="11" width="14" height="6"/>
          <rect class="icon-disc" x="9" y="15" width="8" height="5"/>
        </svg>
      </li>
      <li class="contact-item">
        <span>lorna@tbrennicklaw.example</span>
        <svg class="contact-icon" viewBox="0 0 26 26" aria-label="Email">
          <circle class="icon-disc" cx="13" cy="13" r="13"/>
          <rect class="icon-glyph" x="6" y="8" width="14" height="10"/>
          <polyline class="icon-cut" points="6,8 13,14 20,8"/>
        </svg>
      </li>
      <li class="contact-item">
        <span>http://www.tbrennicklaw.example</span>
        <svg class="contact-icon" viewBox="0 0 26 26" aria-label="Website">
          <circle class="icon-disc" cx="13" cy="13" r="13"/>
          <circle class="icon-line" cx="13" cy="13" r="7"/>
          <ellipse class="icon-line" cx="13" cy="13" rx="3" ry="7"/>
          <line class="icon-line" x1="6" y1="13" x2="20" y2="13"/>
        </svg>
      </li>
    </ul>
  </article>
</main>
</body>
</html>
```